Looking for a website design for my company
Services we offer:
Phone Repair
TV Mounting
Security Camera Installation
Networking / Wi-Fi
Smart Home Services
IT Support

Looking for a website similar to qarnel.com

Few tabs
About Us
Contact Us
Areas Served
Pricing and Services

```html
<!DOCTYPE html>
<html lang="en">
<head>
<meta charset="utf-8">
<title>Vanto Rim — Service and Repair</title>
<link href="https://fonts.googleapis.com/css2?family=Roboto:wght@400;500;700&family=Tinos&display=swap" rel="stylesheet">
<style>
:root{
  --orange:#f15a24;
  --dark:#1f1f21;
  --ink:#222;
  --muted:#555;
  --light:#f7f7f7;
  --stage:#8a8a8d;
  --white:#fff;
}
*{margin:0;padding:0;box-sizing:border-box}
html,body{width:1200px;height:1200px;overflow:hidden;background:var(--stage);font-family:'Roboto',sans-serif;color:var(--ink)}
.page{position:absolute;left:352px;top:0;width:620px;height:1500px;background:var(--white);transform:scale(.8);transform-origin:0 0;overflow:hidden}
.abs{position:absolute}
.topbar{top:0;left:0;width:620px;height:18px;display:flex;justify-content:center;gap:22px;align-items:center;font-size:5px;color:#333}
.topbar span{display:flex;align-items:center;gap:3px}
.topbar i{display:inline-block;width:5px;height:4px;background:var(--orange);border-radius:1px}
.header{top:18px;left:0;width:620px;height:38px;background:var(--orange);display:flex;align-items:center;justify-content:center}
.brand{font-weight:700;font-size:17px;color:#ffd9c2;letter-spacing:.3px}
.nav{top:56px;left:0;width:620px;height:17px;background:var(--dark);display:flex;align-items:center;justify-content:center;gap:16px;font-size:5px;font-weight:700;color:var(--white)}
.nav .active{border-bottom:1.5px solid var(--orange);padding-bottom:2px}
.nav .dd::after{content:" ▾";font-size:4px}
.nav .search{position:absolute;left:451px;top:5px;width:5px;height:5px;border:1px solid #fff;border-radius:50%}
.hero{top:73px;left:0;width:620px;height:220px;background:linear-gradient(115deg,#3c4048,#5a5f66 45%,#3a3e45 70%,#6e6a52);clip-path:polygon(0 0,100% 0,100% 211px,386px 211px,380px 220px,0 220px)}
.hero-copy{left:157px;top:140px;color:var(--white)}
.hero-copy h1{font-size:17px;font-weight:500;margin-bottom:9px}
.hero-copy p{font-size:6.5px;line-height:12px}
.btn-outline{display:inline-block;margin-top:4px;border:1px solid #fff;font-size:5px;padding:4px 12px;color:#fff}
h2.title{font-size:11px;font-weight:500;letter-spacing:.2px}
.rule{width:22px;height:1px;background:var(--ink);margin-top:8px}
.rule.orange{background:var(--orange)}
.rule.white{background:#fff}
.who{left:120px;top:326px;width:380px}
.cols{display:flex;gap:14px;margin-top:18px;font-family:'Tinos',serif;font-size:5.2px;line-height:8px;color:#333}
.cols p{width:183px}
.btn{display:inline-block;background:var(--orange);color:#fff;font-size:5px;padding:5px 12px;margin-top:7px}
.band-dark{left:0;width:620px;background:var(--dark)}
.why{top:469px;height:161px;clip-path:polygon(0 8px,240px 8px,246px 0,100% 0,100% 152px,386px 152px,380px 161px,0 161px)}
.why-in{left:119px;top:32px;color:#fff;width:390px}
.features{display:flex;gap:10px;margin-top:20px}
.feature{display:flex;gap:8px;width:125px}
.feature svg{flex:none;width:22px;height:22px;margin-top:4px}
.feature h3{font-size:6.2px;font-weight:400;margin-bottom:4px}
.feature p{font-size:4.4px;line-height:8px;color:#ddd}
.services{top:621px;left:0;width:620px;height:339px;background:var(--light)}
.services-in{left:120px;top:40px;width:380px}
.lead{font-size:4.6px;color:#333;margin-top:18px}
.grid{display:grid;grid-template-columns:repeat(3,121px);gap:9px 9px;margin-top:17px}
.tile{position:relative;height:82px}
.tag{position:absolute;left:0;bottom:8px;background:var(--orange);color:#fff;font-size:4.6px;line-height:5px;padding:3px 12px 3px 6px;clip-path:polygon(0 0,100% 0,90% 100%,0 100%)}
.news{left:120px;top:995px;width:382px}
.cards{display:flex;gap:9px;margin-top:17px}
.card{width:121px}
.card .img{height:88px;background:linear-gradient(135deg,#0a4fa0,#1f7fd6 50%,#0b3d7c)}
.card h4{font-size:7.5px;font-weight:500;margin:6px 0 5px}
.card .date{font-size:4px;font-weight:700;margin-bottom:5px}
.card p{font-size:4.3px;line-height:8px;color:#444}
.testi{top:1248px;height:161px;clip-path:polygon(0 8px,240px 8px,246px 0,100% 0,100% 152px,386px 152px,380px 161px,0 161px)}
.testi-in{left:119px;top:30px;color:#fff;width:390px}
.quotes{display:flex;gap:22px;margin-top:16px}
.quote{display:flex;gap:8px;width:185px}
.avatar{flex:none;width:46px;height:46px;border-radius:50%;border:2px solid #fff;background:radial-gradient(circle at 50% 40%,#d9b9a0,#6b5447 70%,#3a3a3a)}
.quote p{font-size:4.3px;line-height:8px;color:#ddd}
.quote .who-name{font-size:4px;font-weight:700;color:#fff;margin-top:3px;margin-left:6px}
.dots{display:flex;gap:6px;margin-top:14px}
.dots b{width:4px;height:4px;border-radius:50%;background:#fff}
.dots b:first-child{background:var(--orange)}
.footer{left:0;top:1448px;width:620px;text-align:center}
.footer .brand{color:#8a8a8a;font-size:17px}
.footer p{font-size:4.6px;color:#888;margin-top:8px}
</style>
</head>
<body>
<div class="page">
  <div class="abs topbar">
    <span><i></i>hello@vantorim.net</span>
    <span><i style="border-radius:50%;background:#ccc"></i>Mon-Sat: 7:00-19:00</span>
    <span><i></i>1-800-555-0142</span>
  </div>
  <header class="abs header"><span class="brand">Vanto Rim</span></header>
  <nav class="abs nav">
    <span class="active">Home</span><span class="dd">About Us</span><span class="dd">Contact</span><span class="dd">Areas Served</span><span class="dd">Pricing and Services</span>
    <span class="search"></span>
  </nav>
  <section class="abs hero" role="img" aria-label="Workbench photo with repair tools, pliers and a caliper"></section>
  <div class="abs hero-copy">
    <h1>Service and Repair</h1>
    <p>Lorem Ipsum is simply dummy text of the printing and typesetting industry.<br>Lorem Ipsum has been the industry's</p>
    <span class="btn-outline">LEARN MORE</span>
  </div>

  <section class="abs who">
    <h2 class="title">WHO WE ARE</h2><div class="rule"></div>
    <div class="cols">
      <p>Lorem Ipsum is simply dummy text of the printing and typesetting industry. Lorem Ipsum has been the industry's Lorem Ipsum has been the industry's Lorem Ipsum has been the industry's Lorem Ipsum has been.<br>Lorem Ipsum is simply dummy text of the printing and typesetting industry. Lorem Ipsum has been the industry's Lorem Ipsum has been the industry's Lorem Ipsum has been the industry's Lorem Ipsum has been the industry's Lorem Ipsum has been the industry's</p>
      <p>Lorem Ipsum is simply dummy text of the printing and typesetting industry. Lorem Ipsum has been the industry's Lorem Ipsum has been the industry's Lorem Ipsum has been the industry's Lorem Ipsum has been.<br>Lorem Ipsum is simply dummy text of the printing and typesetting industry. Lorem Ipsum has been the industry's Lorem Ipsum has been the industry's Lorem Ipsum has been the industry's Lorem Ipsum has been the industry's Lorem Ipsum has been the industry's</p>
    </div>
    <span class="btn">LEARN MORE</span>
  </section>

  <section class="abs band-dark why">
    <div class="abs why-in">
      <h2 class="title">WHY CHOOSE US</h2><div class="rule white"></div>
      <div class="features">
        <div class="feature">
          <svg viewBox="0 0 24 24"><polygon fill="#f15a24" points="12,1 15,9 23,9 16.5,14 19,22 12,17 5,22 7.5,14 1,9 9,9"/></svg>
          <div><h3>We are fair and affordable</h3><p>Lorem Ipsum has been the industry's Lorem Ipsum has been the industry's Lorem Ipsum has been the industry's Lorem Ipsum has been the industry's Lorem Ipsum has been the industry's</p></div>
        </div>
        <div class="feature">
          <svg viewBox="0 0 24 24"><path fill="#f15a24" d="M12 2c1 4 6 6 6 12a6 6 0 0 1-12 0c0-3 2-5 3-6 0 2 1 3 2 3 0-3-1-6 1-9z"/></svg>
          <div><h3>Good reputation</h3><p>Lorem Ipsum has been the industry's Lorem Ipsum has been the industry's Lorem Ipsum has been the industry's Lorem Ipsum has been the industry's Lorem Ipsum has been the industry's</p></div>
        </div>
        <div class="feature">
          <svg viewBox="0 0 24 24"><rect x="4" y="2" width="2" height="20" fill="#f15a24"/><path fill="#f15a24" d="M6 3h14l-4 5 4 5H6z"/></svg>
          <div><h3>Our experience</h3><p>Lorem Ipsum has been the industry's Lorem Ipsum has been the industry's Lorem Ipsum has been the industry's Lorem Ipsum has been the industry's Lorem Ipsum has been the industry's</p></div>
        </div>
      </div>
    </div>
  </section>

  <section class="abs services" style="z-index:-1"></section>
  <section class="abs services-in" style="top:661px">
    <h2 class="title">OUR SERVICES</h2><div class="rule orange"></div>
    <p class="lead">Lorem Ipsum is simply dummy text of the printing and typesetting industry. Lorem Ipsum has been the industry's</p>
    <div class="grid">
      <div class="tile" role="img" aria-label="Technician repairing a phone circuit board" style="background:linear-gradient(135deg,#e9e9e9,#9aa3ad 55%,#3b4047)"><span class="tag">Phone Repair</span></div>
      <div class="tile" role="img" aria-label="Technician mounting a TV on a wall" style="background:linear-gradient(135deg,#f2f2f2,#6d6258 60%,#3a3330)"><span class="tag">TV Mounting</span></div>
      <div class="tile" role="img" aria-label="Security camera being installed under a roof" style="background:linear-gradient(135deg,#cfd6da,#8aa8b8 50%,#4a7a96)"><span class="tag">Security Camera<br>Installation</span></div>
      <div class="tile" role="img" aria-label="Router, laptops and globe for networking" style="background:linear-gradient(135deg,#ffffff,#cfd8e4 55%,#4b5a70)"><span class="tag">Networking / Wi-Fi</span></div>
      <div class="tile" role="img" aria-label="Hand touching smart home interface" style="background:linear-gradient(135deg,#b8c6d6,#6a7f98 50%,#2f3e52)"><span class="tag">Smart Home<br>Services</span></div>
      <div class="tile" role="img" aria-label="Blue support network graphic" style="background:linear-gradient(135deg,#0a4fa0,#1f7fd6 50%,#0b3d7c)"><span class="tag">IT Support</span></div>
    </div>
  </section>

  <section class="abs news">
    <h2 class="title">LATEST NEWS</h2><div class="rule orange"></div>
    <div class="cards">
      <article class="card"><div class="img" role="img" aria-label="Blue support network graphic"></div><h4>News Title Here</h4><div class="date">News DateHere</div><p>Lorem Ipsum is simply dummy text of the printing and typesetting industry. Lorem Ipsum has been the industry's Lorem Ipsum is simply dummy text of the printing and typesetting industry. Lorem Ipsum has been the industry's</p></article>
      <article class="card"><div class="img" role="img" aria-label="Blue support network graphic"></div><h4>News Title Here</h4><div class="date">News DateHere</div><p>Lorem Ipsum is simply dummy text of the printing and typesetting industry. Lorem Ipsum has been the industry's Lorem Ipsum is simply dummy text of the printing and typesetting industry. Lorem Ipsum has been the industry's</p></article>
      <article class="card"><div class="img" role="img" aria-label="Blue support network graphic"></div><h4>News Title Here</h4><div class="date" style="margin-top:9px">News DateHere</div><p>Lorem Ipsum is simply dummy text of the printing and typesetting industry. Lorem Ipsum has been the industry's Lorem Ipsum is simply dummy text of the printing and</p></article>
    </div>
  </section>

  <section class="abs band-dark testi">
    <div class="abs testi-in">
      <h2 class="title">TESTIMONIALS</h2><div class="rule white"></div>
      <div class="quotes">
        <div class="quote"><div class="avatar" role="img" aria-label="Customer portrait"></div><div><p>Lorem Ipsum is simply dummy text of the printing and typesetting industry. Lorem Ipsum has been the industry's Lorem Ipsum is simply dummy text of the printing and type setting industry. Lorem Ipsum has been the industry's Lorem</p><div class="who-name">- Coustmer Name</div></div></div>
        <div class="quote"><div class="avatar" role="img" aria-label="Customer portrait"></div><div><p>Lorem Ipsum is simply dummy text of the printing and typesetting industry. Lorem Ipsum has been the industry's Lorem Ipsum is simply dummy text of the printing and type setting industry. Lorem Ipsum has been the industry's Lorem</p><div class="who-name">- Coustmer Name</div></div></div>
      </div>
      <div class="dots"><b></b><b></b><b></b></div>
    </div>
  </section>

  <footer class="abs footer">
    <span class="brand">Vanto Rim</span>
    <p>@ 2020 All Rights Reserved Terms Of Use and Privacy Policy</p>
  </footer>
</div>
</body>
</html>
```